8 x 8 Social Media Design - Tax, Accounting & Bookkeeping Service

Bright Ledger Advisory Group, Inc.

Tax, Accounting and Bookkeeping Services

“We provide our services, with you next mortgage in mind”

Special pricing available for all Mortgage Loan Customers!!

President / CEO Marcus Delaney

Primary service provider with over 27 years of experience

Call directly for more information: (555) 284-9037

Or email at: mdelaney@brightledgerhq.example

```html
<!DOCTYPE html>
<html lang="en">
<head>
<meta charset="utf-8">
<title>Bright Ledger Advisory Group – Mortgage Customers Social Post</title>
<link rel="stylesheet" href="https://fonts.googleapis.com/css2?family=Anton&family=Montserrat:wght@400;500;700;800;900&display=swap">
<style>
  :root {
    --navy-deep: #12213d;
    --navy-ink: #1b3866;
    --royal-blue: #1f4388;
    --sky-blue: #5f95cb;
    --gold: #a8742c;
    --gold-warm: #b07b30;
    --white: #ffffff;
    --photo-light: #e9e6e2;
    --photo-warm: #cdbfb2;
    --photo-shadow: #8b8580;
  }
  * { margin: 0; padding: 0; box-sizing: border-box; }
  html, body {
    width: 1192px; height: 1200px; overflow: hidden;
    background: var(--white);
  }
  .post {
    position: relative; width: 1192px; height: 1200px; overflow: hidden;
    font-family: "Montserrat", Arial, sans-serif; color: var(--white);
    background: var(--sky-blue);
  }
  .hero-photo {
    position: absolute; left: 0; top: 0; width: 1192px; height: 753px;
    background:
      radial-gradient(ellipse 380px 320px at 830px 360px, #c9a58f 0%, rgba(201,165,143,0) 70%),
      linear-gradient(100deg, var(--photo-light) 0%, #dcd6cf 35%, var(--photo-warm) 62%, var(--photo-shadow) 100%);
  }
  .brand {
    position: absolute; left: 56px; top: 150px; width: 340px;
    display: flex; align-items: center; gap: 12px;
  }
  .brand-dot {
    flex: none; width: 34px; height: 34px; border-radius: 50%;
    background: var(--royal-blue);
  }
  .brand-name {
    font-weight: 800; font-size: 24px; line-height: 1.15; color: var(--royal-blue);
  }
  .headline-panel {
    position: absolute; left: 188px; top: 401px; width: 1004px; height: 352px;
    background: rgba(16, 30, 58, 0.86);
  }
  .service-line {
    position: absolute; left: 68px; top: 40px;
    font-size: 21px; font-weight: 500; letter-spacing: 0.2px;
  }
  .headline {
    position: absolute; left: 66px; top: 78px;
    font-family: "Anton", "Oswald", Impact, sans-serif; font-weight: 400;
    font-size: 80px; letter-spacing: 1.5px; white-space: nowrap;
  }
  .headline-line { display: block; height: 77px; line-height: 77px; }
  .headline .highlight {
    display: inline-block; line-height: 72px;
    background: var(--gold); padding: 0 14px 0 8px; margin-left: -8px;
  }
  .lower-shapes { position: absolute; left: 0; top: 753px; }
  .calculator-photo {
    position: absolute; left: 866px; top: 668px; width: 326px; height: 230px;
    background: linear-gradient(150deg, #7f99b6 0%, #c9ccd0 40%, #6d7077 70%, #3a3c41 100%);
    clip-path: polygon(18% 35%, 55% 0, 80% 10%, 100% 45%, 100% 75%, 70% 100%, 0 62%);
  }
  .offer {
    position: absolute; left: 322px; top: 794px;
    font-weight: 800; font-size: 34px; line-height: 45px;
  }
  .contact { position: absolute; left: 308px; top: 1012px; color: var(--navy-ink); }
  .contact-lead { font-size: 22px; font-weight: 400; letter-spacing: 0.3px; }
  .contact-phone { font-size: 44px; font-weight: 800; line-height: 1.1; margin-top: 2px; }
  .contact-email-label { font-size: 21px; font-weight: 400; margin-top: 2px; }
  .contact-email { font-size: 20px; font-weight: 700; margin-top: 4px; }
  .ceo-photo {
    position: absolute; left: 4px; top: 784px; width: 300px; height: 416px;
    background: linear-gradient(180deg, #2a2f3a 0%, #1a1d24 55%, #14161b 100%);
    clip-path: polygon(44% 0, 68% 0, 72% 20%, 94% 32%, 100% 100%, 0 100%, 4% 38%, 38% 22%);
  }
  .ceo-caption {
    position: absolute; left: 80px; top: 1070px; width: 200px;
    text-align: center; font-weight: 700; font-size: 20px; line-height: 27px;
  }
  .experience {
    position: absolute; left: 800px; top: 902px; width: 390px; text-align: center;
  }
  .experience-lead { font-weight: 800; font-size: 29px; line-height: 40px; }
  .experience-years {
    font-weight: 900; font-size: 76px; line-height: 82px; letter-spacing: 1px;
  }
  .experience-tail {
    font-weight: 800; font-size: 44px; line-height: 50px; color: var(--navy-ink);
  }
</style>
</head>
<body>
<main class="post">
  <div class="hero-photo" role="img" aria-label="Photo of a joyful couple celebrating among moving boxes in their new home"></div>

  <div class="brand">
    <span class="brand-dot"></span>
    <span class="brand-name">Bright Ledger Advisory Group, Inc.</span>
  </div>

  <section class="headline-panel">
    <p class="service-line">Tax, Accounting and Bookkeeping Services</p>
    <h1 class="headline">
      <span class="headline-line">We provide our services</span>
      <span class="headline-line">with <span class="highlight">you next</span></span>
      <span class="headline-line"><span class="highlight">mortgage</span> in mind</span>
    </h1>
  </section>

  <svg class="lower-shapes" width="1192" height="447" viewBox="0 0 1192 447" aria-hidden="true">
    <path d="M188 0 H1192 V241 H400 C300 241 225 160 188 0 Z" fill="var(--royal-blue)"/>
    <circle cx="1240" cy="460" r="493" fill="var(--gold-warm)"/>
  </svg>

  <div class="calculator-photo" role="img" aria-label="Photo of a calculator with a small model house on top"></div>

  <p class="offer">Special pricing available<br>for all Mortgage Loan<br>Customers!!</p>

  <div class="ceo-photo" role="img" aria-label="Portrait of the company president wearing a black hat and coat"></div>
  <p class="ceo-caption">President / CEO<br>Marcus Delaney</p>

  <div class="contact">
    <p class="contact-lead">Call directly for more information</p>
    <p class="contact-phone">(555) 284-9037</p>
    <p class="contact-email-label">Or email at:</p>
    <p class="contact-email">mdelaney@brightledgerhq.example</p>
  </div>

  <div class="experience">
    <p class="experience-lead">Primary service<br>provider with over</p>
    <p class="experience-years">27 years</p>
    <p class="experience-tail">of experience</p>
  </div>
</main>
</body>
</html>
```